New Software Development Firm Needs Business Cards!

We just completed a successful logo design project on MakerHive and need to develop a business card design using that shiny new logo. We want a clean, modern design that communicates professionalism and tech savvy without being cliche'.

The company is "Bramble Logic, LLC", but our dba is "Bramble" The business card address should reflect the full company name in the address. The logo just uses "Bramble".

Photoshop or Illustrator source files will be required, along with exact font name(s) and source(s) used.

The design will need to work well with our letterhead as well. I'm also launching a project right now for letterhead and envelopes as well. Please submit to both projects! We're excited to see the designs. Thanks...

Target Market(s)

Small to medium business professionals

Industry/Entity Type

Business

Requirements
Must have
• Need place for:
- Company name and address (5 lines)
- Phone: (1 number)
- Fax: (1 number)
- Employee's name
- Employee's position
- Employee's email address
- Company web site URL
Nice to have
• Probably want a white card, but we're open to options.

```html
<!DOCTYPE html>
<html lang="en">
<head>
<meta charset="utf-8">
<title>Bramble Logic, LLC — Business Card</title>
<link rel="stylesheet" href="https://fonts.googleapis.com/css2?family=Arimo:wght@400&display=swap">
<style>
  :root {
    --sheet-bg: #ffffff;
    --sheet-border: #3a3a3a;
    --card-dark: #000000;
    --card-light: #ffffff;
    --card-edge: #5a5a5a;
    --ink-light: #ffffff;
    --ink-dark: #000000;
    --ink-text: #333333;
  }
  * { margin: 0; padding: 0; box-sizing: border-box; }
  html, body {
    width: 1200px; height: 1001px; overflow: hidden;
    background: var(--sheet-bg);
    font-family: "Arimo", Arial, sans-serif;
  }
  .sheet {
    position: relative; width: 1200px; height: 1001px;
    border: 1px solid var(--sheet-border);
  }
  .card { position: absolute; width: 730px; height: 437px; }
  .card-front { left: 39px; top: 35px; background: var(--card-dark); border: 1px solid var(--card-edge); }
  .card-back { left: 430px; top: 528px; background: var(--card-light); border: 2px solid var(--card-edge); }
  .line { position: absolute; line-height: 1; white-space: nowrap; }

  .card-front .wordmark { left: 204px; top: 170px; color: var(--ink-light); font-size: 84px; }
  .card-front .legal-name { left: 204px; top: 249px; color: var(--ink-light); font-size: 27px; }
  .card-front .website { right: 17px; top: 405px; color: var(--ink-light); font-size: 21px; }

  .card-back .wordmark { left: 36px; top: 32px; color: var(--ink-dark); font-size: 57px; }
  .card-back .legal-name { left: 36px; top: 95px; color: var(--ink-text); font-size: 19px; }
  .person-name { left: 404px; top: 150px; color: var(--ink-text); font-size: 36px; }
  .person-role { left: 404px; top: 187px; color: var(--ink-text); font-size: 25px; }
  .contact-block { position: absolute; top: 303px; color: var(--ink-text); font-size: 22px; line-height: 27.7px; font-style: normal; }
  .address { left: 36px; }
  .contact { left: 404px; }
</style>
</head>
<body>
<div class="sheet">
  <section class="card card-front">
    <div class="line wordmark">Bramble</div>
    <div class="line legal-name">Bramble Logic, LLC</div>
    <div class="line website">www.bramblelogic.net</div>
  </section>

  <section class="card card-back">
    <div class="line wordmark">Bramble</div>
    <div class="line legal-name">Bramble Logic, LLC</div>
    <div class="line person-name">Daniel Reyes</div>
    <div class="line person-role">Director</div>
    <address class="contact-block address">
      No 18 Larkfield Street<br>
      207/4 New York City ,<br>
      NY United States<br>
      Pin-604213
    </address>
    <div class="contact-block contact">
      Phone: 05678 3140<br>
      Fax:05678 3140<br>
      Email:daniel@bramblelogic.net
    </div>
  </section>
</div>
</body>
</html>
```